Business Card Design Project

I am community manager and social media strategist. I need a double sided business card with company logo and name. Looking for something professional, elegant but also a little bit original.

• - The logo and the colours are the company colours and a required to stay.
- The size should be: 84 x 55 mm (or 3.30 x 2.16)
- The file size should be: 1039 x 697 pixels (300 dpi)
- I'd like rounded corners. :)

Use the following contact information for the card:

Léonie Vardin
Stratégie médias sociaux / community management / édition de sites sociaux
mob. : 0687529103
leonie.vardin@postelune.fr
Twitter. : @lvardin
Skype : vardin.leonie

```html
<!DOCTYPE html>
<html lang="fr">
<head>
<meta charset="utf-8">
<title>Aveliane – carte de visite</title>
<link href="https://fonts.googleapis.com/css2?family=Open+Sans:wght@300;400;600;700&display=swap" rel="stylesheet">
<style>
  :root {
    --page: #ffffff;
    --card-front: #ffffff;
    --brand: #1f6896;
    --brand-mid: #2a6aa0;
    --brand-deep: #174a7c;
    --ink: #1c1c1c;
    --ink-soft: #555a5e;
    --icon: #1f6896;
  }
  * { margin: 0; padding: 0; box-sizing: border-box; }
  html, body { width: 1200px; height: 900px; overflow: hidden; background: var(--page); }
  body { position: relative; font-family: "Open Sans", Arial, sans-serif; }

  .card {
    position: absolute;
    width: 648px;
    height: 424px;
    border-radius: 46px;
    overflow: hidden;
    box-shadow: 6px 10px 14px rgba(0,0,0,0.28);
  }
  .card-back { left: 480px; top: 403px; background: var(--brand-mid); }
  .card-back .swoosh { position: absolute; inset: 0; width: 100%; height: 100%; }
  .card-front { left: 60px; top: 72px; background: var(--card-front); z-index: 2; box-shadow: 6px 10px 16px rgba(0,0,0,0.32); }

  .brand-lockup {
    position: absolute;
    display: flex;
    flex-direction: column;
    align-items: center;
    gap: 14px;
  }
  .brand-mark { border-radius: 50%; }
  .brand-name { font-weight: 600; letter-spacing: 1px; line-height: 1; }

  .card-front .brand-lockup { left: 70px; top: 136px; width: 200px; }
  .card-front .brand-mark { width: 94px; height: 94px; background: var(--brand); }
  .card-front .brand-name { font-size: 38px; color: var(--brand); }

  .card-back .brand-lockup { left: 225px; top: 143px; width: 200px; }
  .card-back .brand-mark { width: 94px; height: 94px; background: #ffffff; }
  .card-back .brand-name { font-size: 38px; color: #ffffff; }

  .holder { position: absolute; left: 340px; top: 74px; }
  .holder-name { font-size: 22px; font-weight: 700; color: var(--ink); }
  .holder-role { margin-top: 14px; font-size: 17px; font-weight: 300; line-height: 23px; color: var(--ink-soft); }

  .contacts { position: absolute; left: 340px; top: 294px; list-style: none; }
  .contacts li { display: flex; align-items: center; gap: 7px; font-size: 17.5px; font-weight: 300; line-height: 23px; color: var(--ink-soft); }
  .contacts svg { width: 14px; height: 14px; flex: none; }
</style>
</head>
<body>

<section class="card card-back" aria-label="Verso de la carte">
  <svg class="swoosh" viewBox="0 0 648 424" preserveAspectRatio="none" aria-hidden="true">
    <defs>
      <linearGradient id="deepCorner" x1="0.3" y1="0.2" x2="1" y2="1">
        <stop offset="0" stop-color="#2a6aa0" stop-opacity="0"/>
        <stop offset="1" stop-color="#174a7c"/>
      </linearGradient>
    </defs>
    <path d="M0 105 C 290 150, 520 260, 634 412 L 648 424 L 648 0 L 0 0 Z" fill="url(#deepCorner)"/>
  </svg>
  <div class="brand-lockup">
    <span class="brand-mark"></span>
    <span class="brand-name">AVELIANE</span>
  </div>
</section>

<section class="card card-front" aria-label="Recto de la carte">
  <div class="brand-lockup">
    <span class="brand-mark"></span>
    <span class="brand-name">AVELIANE</span>
  </div>

  <div class="holder">
    <h1 class="holder-name">Léonie Vardin</h1>
    <p class="holder-role">Stratégie médias sociaux /<br>Community management /<br>Édition de sites sociaux</p>
  </div>

  <ul class="contacts">
    <li>
      <svg viewBox="0 0 14 14" aria-label="Mobile"><rect x="3" y="0.8" width="8" height="12.4" rx="1.6" fill="none" stroke="var(--icon)" stroke-width="1.6"/><rect x="5.5" y="10.3" width="3" height="1.2" fill="var(--icon)"/></svg>
      068 752 9103
    </li>
    <li>
      <svg viewBox="0 0 14 14" aria-label="E-mail"><rect x="0.8" y="2.5" width="12.4" height="9" rx="1" fill="none" stroke="var(--icon)" stroke-width="1.5"/><path d="M1.2 3.2 L7 8 L12.8 3.2" fill="none" stroke="var(--icon)" stroke-width="1.5"/></svg>
      leonie.vardin@postelune.fr
    </li>
    <li>
      <svg viewBox="0 0 14 14" aria-label="Réseau social"><rect x="1" y="1" width="12" height="12" rx="2.5" fill="var(--icon)"/></svg>
      @lvardin
    </li>
    <li>
      <svg viewBox="0 0 14 14" aria-label="Messagerie"><circle cx="7" cy="7" r="6.2" fill="var(--icon)"/></svg>
      vardin.leonie
    </li>
  </ul>
</section>

</body>
</html>
```